We would like to incorporate our logo into letterhead design and envelopes. We are looking for something that is moderately conservative but not old law firm style. Both the envelopes and the letterhead must have both firm addresses. We would like to incorporate the color of the logo, but only a small amount of color - perhaps on one of the borders. The addresses for the firm locations are listed below. Given that it is a law firm, it needs to somewhat conservative, but not the old school, small black font on cream colored paper design.

The firm addresses are:

27815 N. Harlow Pemberton Pkwy.
Ste 4200
Scottsdale, AZ 85391

6100 W. Cedar Avenue
Ste 700
Burbank, CA 91623

Industry/Entity Type

Legal

Colors

Designer to choose colors to be used in the design.

Requirements
Must have
• Both addresses:
• 27815 N. Harlow Pemberton Pkwy.
• Ste 4200
• Scottsdale, AZ 85391
• 6100 W. Cedar Avenue
• Ste 700
• Burbank, CA 91623
Nice to have
• Small amount of color on border(s) that matches the logo but not too much color

```html
<!DOCTYPE html>
<html lang="en">
<head>
<meta charset="utf-8">
<title>Meridale Law — Letterhead and Envelopes</title>
<link rel="stylesheet" href="https://fonts.googleapis.com/css2?family=Marcellus&family=Roboto+Condensed:wght@400&display=swap">
<style>
  :root {
    --backdrop: #c8c8c8;
    --paper: #ebe7e0;
    --navy: #27235e;
    --watermark: #d3d0cc;
    --rule: #c9c6c2;
    --ink: #2b2b33;
    --white: #ffffff;
  }
  * { box-sizing: border-box; margin: 0; padding: 0; }
  html, body {
    width: 1200px; height: 800px; overflow: hidden;
    background: var(--backdrop);
  }
  .stationery-set { position: relative; width: 1200px; height: 800px; }

  .sheet {
    position: absolute;
    background: var(--paper);
    overflow: hidden;
    box-shadow: 0 2px 6px rgba(0,0,0,0.18);
  }

  .firm-name {
    font-family: "Marcellus", serif;
    color: var(--navy);
    font-weight: 400;
    letter-spacing: 0.02em;
    white-space: nowrap;
    position: absolute;
  }

  .watermark-name {
    position: absolute;
    font-family: "Marcellus", serif;
    color: var(--watermark);
    white-space: nowrap;
    transform-origin: left top;
    transform: rotate(-90deg);
    letter-spacing: 0.02em;
    line-height: 1;
  }
  .watermark-rule {
    position: absolute;
    width: 1px;
    background: var(--rule);
  }

  .address-block {
    position: absolute;
    display: flex;
    align-items: stretch;
    font-family: "Roboto Condensed", sans-serif;
    color: var(--ink);
    line-height: 1.3;
  }
  .address-block .office { white-space: nowrap; }
  .address-block .divider {
    width: 1px;
    background: var(--navy);
  }
  .accent-square { position: absolute; left: 0; background: var(--navy); }
  .bottom-band { position: absolute; left: 0; right: 0; background: var(--navy); }

  /* Letterhead */
  .letterhead { left: 170px; top: 105px; width: 420px; height: 594px; }
  .letterhead .firm-name { left: 33px; top: 50px; font-size: 27px; }
  .letterhead .watermark-name { left: 330px; top: 560px; font-size: 54px; }
  .letterhead .watermark-rule { left: 392px; top: 27px; height: 533px; }
  .letterhead .accent-square { top: 534px; width: 34px; height: 27px; }
  .letterhead .address-block { left: 43px; top: 533px; font-size: 8px; }
  .letterhead .address-block .divider { margin: 0 10px; }
  .letterhead .bottom-band { bottom: 2px; height: 6px; }

  /* Envelope back */
  .envelope-back { left: 640px; top: 150px; width: 420px; height: 200px; }
  .envelope-flap { position: absolute; left: 0; top: 0; width: 420px; height: 58px; }
  .envelope-back .firm-name {
    color: var(--white);
    font-size: 14px;
    left: 0; right: 0; top: 20px;
    text-align: center;
  }

  /* Envelope front */
  .envelope-front { left: 640px; top: 430px; width: 420px; height: 200px; }
  .envelope-front .firm-name { left: 24px; top: 28px; font-size: 24px; }
  .envelope-front .watermark-name { left: 354px; top: 196px; font-size: 30px; }
  .envelope-front .watermark-rule { left: 392px; top: 4px; height: 192px; }
  .envelope-front .accent-square { top: 155px; width: 24px; height: 22px; }
  .envelope-front .address-block { left: 33px; top: 155px; font-size: 7px; }
  .envelope-front .address-block .divider { margin: 0 10px; }
  .envelope-front .bottom-band { bottom: 1px; height: 4px; }
</style>
</head>
<body>
<main class="stationery-set">

  <section class="sheet letterhead" aria-label="Letterhead">
    <h1 class="firm-name">MERIDALE LAW</h1>
    <span class="watermark-name" aria-hidden="true">MERIDALE LAW</span>
    <span class="watermark-rule"></span>
    <span class="accent-square"></span>
    <address class="address-block">
      <div class="office">27815 N. Harlow Pemberton Pkwy.<br>Ste 4200<br>Scottsdale, AZ 85391</div>
      <span class="divider"></span>
      <div class="office">6100 W. Cedar Avenue<br>Ste 700<br>Burbank, CA 91623</div>
    </address>
    <span class="bottom-band"></span>
  </section>

  <section class="sheet envelope-back" aria-label="Envelope back">
    <svg class="envelope-flap" viewBox="0 0 420 58" aria-hidden="true">
      <path d="M0 0 H420 V8 Q418 34 398 50 Q390 57 376 57 H44 Q30 57 22 50 Q2 34 0 8 Z" fill="var(--navy)"/>
    </svg>
    <p class="firm-name">MERIDALE LAW</p>
  </section>

  <section class="sheet envelope-front" aria-label="Envelope front">
    <p class="firm-name">MERIDALE LAW</p>
    <span class="watermark-name" aria-hidden="true">MERIDALE</span>
    <span class="watermark-rule"></span>
    <span class="accent-square"></span>
    <address class="address-block">
      <div class="office">27815 N. Harlow Pemberton Pkwy.<br>Ste 4200<br>Scottsdale, AZ 85391</div>
      <span class="divider"></span>
      <div class="office">6100 W. Cedar Avenue<br>Ste 700<br>Burbank, CA 91623</div>
    </address>
    <span class="bottom-band"></span>
  </section>

</main>
</body>
</html>
```